4"x9" Roofing Flyer Design - Tile Roofing!

We are looking to create a 4"x9" double sided flyer in full color that displays pictures of before and after of tile underlayment replacement. This would have words as well.

The theme should match the overall theme of our brochure that we already have designed so they are cohesive.

I have uploaded an example of a similar flyer that we like the overall layout of.

Please read the "Design Wording" PDF I uploaded for the words and overall design layout we are looking for on this brochure.

Please let me know if you'd like more photos or anything like that.

Target Market(s)

Retirees

Industry/Entity Type

Roofing

Font styles to use
Other font styles liked:
• Match existing fonts from our brochure

Requirements
Must have
• Must match style of existing brochure (uploaded), font must match closely as well

```html
<!DOCTYPE html>
<html lang="en">
<head>
<meta charset="utf-8">
<title>Cedarline Roofing – Tile Underlayment Flyer</title>
<link href="https://fonts.googleapis.com/css2?family=Poppins:wght@400;500;600;700;800&display=swap" rel="stylesheet">
<style>
  :root{
    --stage:#d0d0d0;
    --ink:#0c0e12;
    --orange:#e4571d;
    --white:#ffffff;
    --badge:#4a4f57;
  }
  *{box-sizing:border-box;margin:0;padding:0}
  html,body{width:1200px;height:1194px;overflow:hidden;background:var(--stage);font-family:"Poppins",sans-serif;color:var(--white)}
  .flyer{position:absolute;top:120px;width:424px;height:954px;background:linear-gradient(180deg,#1a1f27 0%,#11151b 30%,#0b0d10 100%);overflow:hidden}
  .flyer--front{left:138px}
  .flyer--back{left:637px}
  .brand{position:absolute;top:110px;left:0;width:100%;text-align:center;font-weight:700;font-size:36px;line-height:1;letter-spacing:.2px}
  .brand-dot{display:inline-block;width:14px;height:14px;background:var(--orange);margin-right:10px;vertical-align:middle;position:relative;top:-4px}
  .phone{position:absolute;top:160px;left:0;width:100%;text-align:center;font-weight:700;font-size:38px;letter-spacing:4px;color:var(--orange);line-height:1}
  .hero{position:absolute;left:0;top:0;width:424px;height:560px}
  .badge{position:absolute;left:55px;top:238px}
  .before-label{position:absolute;left:188px;top:353px;font-weight:700;font-size:30px;letter-spacing:1px}
  .compare{position:absolute;left:30px;top:431px;width:364px;height:154px;display:flex}
  .compare-shot{position:relative;width:182px;height:154px}
  .compare-tag{position:absolute;top:0;left:0;height:25px;width:117px;background:var(--orange);clip-path:polygon(0 0,88% 0,100% 100%,0 100%);font-weight:700;font-size:15px;line-height:25px;padding-left:21px}
  .copy{position:absolute;left:30px;width:366px;font-size:10.8px;line-height:12.6px;letter-spacing:-.15px}
  .copy h2{color:var(--orange);font-weight:700;font-size:18.5px;line-height:20px;letter-spacing:0;text-transform:uppercase;margin-bottom:13px}
  .copy p{margin-bottom:12px;text-align:justify}
  .copy .term{color:var(--orange);font-weight:700;display:block}
  .copy .item{margin-bottom:8px}
  .rule{height:1.5px;background:var(--orange);margin:12px 0 14px}
  .back-copy{width:384px}
  .back-copy p{text-align:left}
  .back-copy .lead{font-weight:600}
  .licence{position:absolute;left:0;top:829px;width:424px;height:45px;background:var(--orange);text-align:center;font-weight:700;font-size:25px;line-height:45px;letter-spacing:.5px}
  .web{position:absolute;left:0;top:884px;width:424px;text-align:center;font-weight:700;font-size:26px;line-height:40px}
</style>
</head>
<body>

<section class="flyer flyer--front">
  <svg class="hero" viewBox="0 0 424 560">
    <defs>
      <linearGradient id="debris" x1="0" y1="0" x2="0" y2="1">
        <stop offset="0" stop-color="#6e6458"/>
        <stop offset=".5" stop-color="#4a4239"/>
        <stop offset="1" stop-color="#15181c"/>
      </linearGradient>
    </defs>
    <polygon role="img" aria-label="Photo of crumbling old roof underlayment before replacement" points="0,392 322,232 424,288 424,560 0,560" fill="url(#debris)"/>
    <polygon points="0,370 322,215 424,270 424,285 322,232 0,392" fill="var(--orange)"/>
    <polyline points="0,392 322,232 424,288" fill="none" stroke="#fff" stroke-width="2"/>
  </svg>
  <svg class="badge" width="160" height="165" viewBox="0 0 160 165" role="img" aria-label="Certification badge placeholder">
    <polygon points="80,0 160,82 80,165 0,82" fill="var(--badge)"/>
  </svg>

  <div class="brand"><span class="brand-dot"></span>Cedarline Roofing</div>
  <div class="phone">555-214-7730</div>
  <div class="before-label">BEFORE</div>

  <div class="compare">
    <div class="compare-shot">
      <svg width="182" height="154" role="img" aria-label="Photo of new underlayment with tiles stacked during re-lay"><defs><linearGradient id="during" x1="0" y1="0" x2="0" y2="1"><stop offset="0" stop-color="#4f7fd6"/><stop offset=".4" stop-color="#2b3550"/><stop offset="1" stop-color="#d9dde6"/></linearGradient></defs><rect width="182" height="154" fill="url(#during)"/></svg>
      <div class="compare-tag">DURING</div>
    </div>
    <div class="compare-shot">
      <svg width="182" height="154" role="img" aria-label="Photo of finished tile roof after re-lay"><defs><linearGradient id="after" x1="0" y1="0" x2="0" y2="1"><stop offset="0" stop-color="#b7a38a"/><stop offset=".5" stop-color="#9a8a76"/><stop offset="1" stop-color="#7a6c5d"/></linearGradient></defs><rect width="182" height="154" fill="url(#after)"/></svg>
      <div class="compare-tag">AFTER</div>
    </div>
  </div>

  <div class="copy" style="top:608px">
    <h2>The Hidden Clock<br>Ticking Under Your Tiles</h2>
    <p>When a tile roof is installed, the tiles themselves are not waterproof—they are simply a shield. The actual waterproofing is done by the felt or synthetic underlayment installed beneath them.</p>
    <p style="margin-bottom:0">In homes of your vintage, this underlayment is now:</p>
    <div class="rule"></div>
    <p class="item"><span class="term">Brittle and Chalky:</span>It cracks and turns into powder under the constant heat cycles, losing its waterproofing integrity.</p>
    <p class="item" style="margin-bottom:0"><span class="term">Compromised:</span>Even a single leak in a neighboring home means the moisture risk has increased exponentially across the entire block.</p>
    <div class="rule"></div>
    <p>Based on the age and materials used in this specific neighborhood, underlayment failure is not a matter of if, but when.</p>
    <p>Waiting for a visible ceiling stain often means the damage has already spread to the roof deck, rafters, and interior walls. A slow leak can silently cost thousands in remediation before you ever see a drop.</p>
  </div>
</section>

<section class="flyer flyer--back">
  <svg class="hero" viewBox="0 0 424 560">
    <defs>
      <linearGradient id="home" x1="0" y1="0" x2="0" y2="1">
        <stop offset="0" stop-color="#5d6a4e"/>
        <stop offset=".45" stop-color="#4a4f55"/>
        <stop offset=".8" stop-color="#1b1e22"/>
        <stop offset="1" stop-color="#0b0d10"/>
      </linearGradient>
    </defs>
    <polygon role="img" aria-label="Aerial photo of a large home with a new roof among pine trees" points="0,392 322,232 424,288 424,500 0,500" fill="url(#home)"/>
    <polygon points="0,370 322,215 424,270 424,285 322,232 0,392" fill="var(--orange)"/>
    <polyline points="0,392 322,232 424,288" fill="none" stroke="#fff" stroke-width="2"/>
  </svg>

  <div class="brand"><span class="brand-dot"></span>Cedarline Roofing</div>
  <div class="phone">555-214-7730</div>

  <div class="copy back-copy" style="top:535px">
    <h2>Our Certified Solution:<br>The Proactive, Full-Service<br>Tile Lift &amp; Re-Lay</h2>
    <p style="margin-bottom:0">We specialize in preserving your beautiful tile roof while replacing the single most important component: the underlayment.</p>
    <div class="rule" style="margin:19px 0 22px;width:366px"></div>
    <p class="lead" style="margin-bottom:14px">As a licensed, bonded, and insured local contractor, we don't just replace the felt; we ensure your entire roof is built to perform:</p>
    <p class="item" style="margin-bottom:12px"><span class="term">Careful Tile Removal:</span>Each tile is removed by hand, inspected, and saved.</p>
    <p class="item" style="margin-bottom:12px"><span class="term">Deck Inspection:</span>We check for and address any underlying damage or rot.</p>
    <p class="item" style="white-space:nowrap"><span class="term">Premium Underlayment:</span>We install a modern, high-grade self-adhered synthetic underlayment.</p>
  </div>

  <div class="licence">AZ ROC 271605</div>
  <div class="web">www.cedarline-roofing.com</div>
</section>

</body>
</html>
```